Online Psychiatry business - Business Card

I need a business card design. The target audience is busy professionals of any field (this therapy appeals best to 24-35 year olds). It involves psychiatry by tele-medicine (or video-conference). Nothing on it should be a giveaway that it's about mental health. Professional design with silver or gold as the primary colors appeals to me. The card must be as simple and as uncluttered as possible. Some color and flowing design on the edge of the card appeals to me.
CrestMindLink.com should probably appear in the center of the card and stand out, i.e. bold lettering, and easy to read, no cursive, but Ariel Black. Some where below this, should appear "Too Busy to Take Care of Yourself? Think again." Since this isn't office based, I don't think an office address is necessary and limits clutter.
Information that does need to appear is my name: Gerald Whitcombe, MD
General phone number: 541-876-2209. I'm hoping to get an 24-hour answering service soon so leave a little room for this. In addition I want to include two email addresses:
CrestMindLink@maildrop-box.com and CrestMind247@maildrop-box.com
Updates

I like the designs. I would like someone to put the website in bold in the center

 as most have been doing with a smaller font reminder nearby saying "No time" etc.
but I'd like to put my name down in the corner with the rest of the contact material.
Black print against a white or grey background appeals to me, with darker silver artwork near the sides (simple abstract, like wavy lines or something you can one up with that works. 
thanks

I ve tried to provide as much feedback as possible given my time limits, so if you have extra questions, please feel free to email. I tried to attach a file of a business card I really like but make be difficult to actually manufacture. I'm going to send you a link to the photo. The card has a pull tab. There is not much information on the outside. In fact, if you were to design the outside, I would just print : Too Busy to Take Care of Yourself? Think Again.

When you pull the tab the remaining information is on the bottom half of the card. Please don't use the color pink!!!!
http://www.layoutgallerypost.com/2009/05/100-clever-card-ideas/
It is the 39th photo on the list, about 2/3ds of the way down the page. It is titled: Faltenkästli

#7 and #16 have an appeal to me, except for the dot patterns
Hope this helps

I'm running out of time and energy. I 've been trying to give do down the list and give  individual feedback but I won't be able to do that anymore.

So if you have any specific questions, write me, and again thank you for all your effort!!

I know i received your files, including your zip files, Plonix,

but Gideon, did you send me the files including ZIP on project 5914386?
thanks

Target Market(s)

Working professionals and executive, attorneys, etc.

Industry/Entity Type

Business

Logo Text

Don't Have Time to Take Care of Yourself? Think Again.

Logo styles of interest
Pictorial/Combination Logo
Wordmark Logo
Other font styles liked:
• Ariel Black appeals to me the most

Requirements
Must have
• Want to emphasize that the website must be obvious, easily found (The CrestMindLink.com)
For that reason i'd like the card to be white, and minimal decoration on one or both sides just to add some style and color
Nice to have
• A Very uncluttered, elegant design, and something that makes it stick in your head-doesn't everyone want the last?
Should not have
• Nothing on the card that give it away that this is about psychiatry, such as brain or other symbol, but also nothing that gives it away as a medical business, such as a stethoscope or red cross or anything.

```html
<!DOCTYPE html>
<html lang="en">
<head>
<meta charset="utf-8">
<title>CrestMindLink.com – Business Card</title>
<link rel="stylesheet" href="https://fonts.googleapis.com/css2?family=Archivo+Black&display=swap">
<style>
  :root {
    --card-grey: #6d6c70;
    --panel-white: #ffffff;
    --ink: #4a4849;
    --ink-light: #f2f2f2;
  }
  html, body {
    margin: 0;
    padding: 0;
    width: 1200px;
    height: 704px;
    overflow: hidden;
    background: var(--card-grey);
  }
  .card {
    position: relative;
    width: 1200px;
    height: 704px;
    background: var(--card-grey);
    font-family: "Archivo Black", "Arial Black", sans-serif;
    color: var(--ink);
  }
  .speech-panel {
    position: absolute;
    inset: 0;
    width: 1200px;
    height: 704px;
  }
  .speech-panel path { fill: var(--panel-white); }
  .card-text {
    position: absolute;
    margin: 0;
    line-height: 1;
    white-space: nowrap;
  }
  .site-name {
    left: 95px;
    top: 158px;
    font-size: 80px;
    letter-spacing: -1px;
  }
  .tagline {
    right: 78px;
    top: 258px;
    font-size: 19px;
  }
  .doctor-name {
    left: 136px;
    top: 340px;
    font-size: 34px;
  }
  .credential {
    left: 141px;
    top: 386px;
    font-size: 16px;
  }
  .phone {
    left: 136px;
    top: 434px;
    font-size: 28px;
  }
  .email {
    top: 656px;
    font-size: 26px;
    color: var(--ink-light);
  }
  .email-main { left: 48px; }
  .email-alt { left: 640px; }
</style>
</head>
<body>
<div class="card">
  <svg class="speech-panel" viewBox="0 0 1087 638" preserveAspectRatio="none" aria-hidden="true">
    <path d="M58,28 H1030 Q1048,28 1048,46 V496 Q1048,514 1030,515 H290 Q262,518 260,545 V586 L252,584 L62,430 Q40,412 40,395 V46 Q40,28 58,28 Z"/>
  </svg>

  <h1 class="card-text site-name">CrestMindLink.com</h1>
  <p class="card-text tagline">"Too Busy to Take Care of Yourself? Think again.”</p>

  <p class="card-text doctor-name">Gerald Whitcombe</p>
  <p class="card-text credential">MD</p>
  <p class="card-text phone">Phone : 541-876-2209</p>

  <p class="card-text email email-main">CrestMindLink@maildrop-box.com</p>
  <p class="card-text email email-alt">CrestMind247@maildrop-box.com</p>
</div>
</body>
</html>
```